依頼概要
現在長崎において高単価の焼肉店『炎楽亭』、食べ放題の焼肉店『炙蔵』運営しております。
この度『赤身肉専門焼肉店』を開店するにあたり開店日よりスタートダッシュを図る為に内装工事開始より『1回目の告知』を致します、工事期間終盤戦に詳細が掲載された『2回目の告知』告知を致します。

『1回目の告知』は詳しい内容は掲載はせずお客様に『何のお店が出来るだろう?』と想像してもらえる程度の内容です、『2回目の告知』にメニューや金額などの詳細が掲載された告知を行います。

こらはお客様の期待感を煽りながら徐々に真相を明らかにしていくというプロダクトローンチと言う宣伝方法です、情報商材などでよく使われている手法です。

『1回目の告知用ポスター』『2回目の告知用ポスター』『店内メニュー作成』『ロゴマーク』は一貫性を持たせた物でないといけませんので同じ方にお願いしたいと思っております、その『1回目の告知ポスター』の御依頼です。
『2回目の告知用ポスター』と『店内メニュー』『ロゴマーク』に関しましては採用させて頂いた方に再依頼をお願い致します。

『1回目の告知ポスター』はお客様に『また炎楽亭が何か作るんだ』とか『今度は何の店だ?』『普通の店じゃないな』と勝手に想像を膨らませて貰う様なイメージ的なものです、現在営業中の各店舗にて『何の店が出来るの?』と聞かれる位で丁度良いと思います。

最低でも『肉屋』もしくは『焼肉屋』位は伝わる必要があると思います、私共が持っている写真素材はダイレクトに分かる物ばかりですので、もし何かしら使える素材をお持ちでしたら写真を使って頂いても結構です、文字だけの物でも構いません。
私が見てインパクトを受け想像が膨らんだ写真を1点、店内の内装の写真を添付しておきますので御参考にされて下さい。

クライアントの意向をよく理解されておりデザインに忠実に反映されていたと思います。

様々な御提案誠にありがとうございました、今後とも依頼を続けていきますので何卒宜しくお願い致します。

```html
<!DOCTYPE html>
<html lang="ja">
<head>
<meta charset="utf-8">
<title>NICE TO MEAT YOU!! 赤身肉 近日公開</title>
<link rel="stylesheet" href="https://fonts.googleapis.com/css2?family=Anton&family=Noto+Sans+JP:wght@900&display=swap">
<style>
  :root {
    --ink: #000000;
    --paper: #ffffff;
    --meat-red: #d4000e;
    --band-red: #d6000f;
    --flame-core: #ffb030;
    --flame-mid: #e8480c;
    --smoke: #9a9a9a;
  }
  html, body {
    margin: 0;
    padding: 0;
    width: 846px;
    height: 1200px;
    overflow: hidden;
    background: var(--ink);
  }
  .poster {
    position: relative;
    width: 846px;
    height: 1200px;
    background: var(--ink);
    overflow: hidden;
  }
  .poster__art {
    position: absolute;
    inset: 0;
    display: block;
  }
  .headline {
    font-family: "Anton", "Oswald", Impact, sans-serif;
    fill: var(--paper);
  }
  .headline--meat {
    fill: var(--meat-red);
  }
  .band {
    fill: var(--band-red);
  }
  .band__title {
    font-family: "Noto Sans JP", sans-serif;
    font-weight: 900;
    fill: var(--paper);
  }
  .band__teaser {
    font-family: "Noto Sans JP", sans-serif;
    font-weight: 900;
    fill: var(--ink);
  }
  .band__tagline {
    font-family: "Anton", "Oswald", Impact, sans-serif;
    fill: var(--ink);
  }
</style>
</head>
<body>
<main class="poster">
  <svg class="poster__art" viewBox="0 0 846 1200" width="846" height="1200" xmlns="http://www.w3.org/2000/svg">
    <defs>
      <linearGradient id="fire-fade" x1="0" y1="1" x2="0" y2="0">
        <stop offset="0" stop-color="var(--flame-core)" stop-opacity="0.55"/>
        <stop offset="0.45" stop-color="var(--flame-mid)" stop-opacity="0.35"/>
        <stop offset="1" stop-color="var(--smoke)" stop-opacity="0"/>
      </linearGradient>
    </defs>

    <text class="headline headline--nice" x="40" y="274" font-size="246" textLength="625" lengthAdjust="spacingAndGlyphs">NICE</text>
    <text class="headline headline--to" x="700" y="163" font-size="118" textLength="95" lengthAdjust="spacingAndGlyphs">T</text>
    <text class="headline headline--to" x="700" y="274" font-size="118" textLength="95" lengthAdjust="spacingAndGlyphs">O</text>

    <g transform="rotate(9 423 520)">
      <text class="headline headline--meat" x="40" y="705" font-size="430" textLength="766" lengthAdjust="spacingAndGlyphs">MEAT</text>
    </g>

    <g class="fire" role="img" aria-label="Flames and smoke rising from the red lettering">
      <rect x="190" y="360" width="90" height="230" rx="45" fill="url(#fire-fade)"/>
      <rect x="470" y="250" width="80" height="210" rx="40" fill="url(#fire-fade)"/>
    </g>

    <text class="headline headline--you" x="40" y="953" font-size="342" textLength="766" lengthAdjust="spacingAndGlyphs">YOU!!</text>

    <rect class="band" x="0" y="990" width="846" height="170"/>
    <text class="band__title" x="22" y="1132" font-size="112" textLength="398" lengthAdjust="spacingAndGlyphs">赤身肉</text>
    <text class="band__teaser" x="452" y="1106" font-size="88" textLength="352" lengthAdjust="spacingAndGlyphs">近日公開</text>
    <text class="band__tagline" x="448" y="1147" font-size="36" textLength="370" lengthAdjust="spacingAndGlyphs">Lean meat coming soon...</text>
  </svg>
</main>
</body>
</html>
```